Major Australian Food and Wine Event Web Design Project

The project will consist of 3 designs
The homepage
A city hub page
A general content page

The main audience who will visit the website will be (in Order of importance:

1) Visitors
- Mainly women 24 – 54 years (they are the main ticket buyers)
- In a relationship – so will go to the show with their partner
- In a good paying job or home maker – and who have disposable income to spend $30 a ticker
- Enjoy food, wine and going out
- Looking for a fun day out – although an event that is about food and wine – it is an event that most people will go to and have a fun day out – not too pretentious

A smaller proportion of the audience will be:
2) Exhibitors & sponsors ( both prospective and existing)
3) Media

Objectives:

- Functionality on home page and sub pages needs to be updated, clear, easy to navigate and inject a sense of ‘fun’ – need to make it look more professional
- Need to incorporate the many things that need to be on the home page and sub pages in a visually appealing manner
- Ensure the ‘Cons’ above are considered and reflected in functionality and design
- To not be too focus on the colours (these can be changed) – but focus on the functionality and overall design opportunities.

Approach:

Keywords to describe the Bright Plate & Vine Fair:
Fun day out, discover, learn, indulge, entertaining

Other website examples:

Some great consumers event websites from the UK really make our website look basic and juvenile – and below are some examples of the presentation of how we would like our website to look like:

http://www.morselfairs-example.com/london/ This website is clean, includes good social media integration and exudes a sense of fun. Their content pages, such as the features landing page also presents options in a clear and visually appealing way with a series of boxes including image and text http://www.morselfairs-example.com/london/content/343/Features

http://www.homecraftexpo-example.com/ - this is also a great website – and it incorporates all the elements we would be looking for on our homepage – but the background/skin also includes a sense of fun and cheekiness. Subpages also are consistent.

Features

• Its a fun day that offers great value for money
• Caters to all visitors, regardless of different levels of knowledge or interest in food, wine and cooking.
• Sample great quality food and wine products from hundreds of reputable exhibitors
• Learn more through many of the shows feature activities (Celeb Theatre, Wine Theatre, Cooking & Cheese Classes)

Functionality & Structure:

In a user friendly, easy to view way, we need to incorporate the following functionality elements on home page:
- main header (that will incorporate our current creative) with a ‘fun’ skin
- navigation tabs/references (hone, location, tickets, blog, sign up, exhibitors)
- navigation/content banner (rotating)
- Area for small intro about the show
- News and highlight section
- New exhibitors section
- Obvious Ticket call to action
- Obvious sign up call to action
- Social media buttons or links ( really like the moving gifs on the Homecraftexpo-example.com site
- area for advertising (MREC size) to sell to exhibitors/sponsors
- Show dates for all 5 shows (maybe in main header)

Subpage layout is also important and needs to reflect the homepage – so would also like to see examples of how this would look and tie in with navigation – we generally have a lot of content on these pages, so clear navigation would be useful. – see below for further details of functionality for city Hubs

‘CITY HUB’ BRIEF
When navigating to each location the user will be taken to a ‘CITY HUB’ which should replicate design and content elements of a main HOME page, as well as reflect more specific information for each Show. Elements which must appear on this page are:
• FEATURES – which may be displayed in categories (in boxes, see appendix 1.0) which will link through to relevant content pages. Or in one box which will link through to a features page with all presented in boxes
• CHEFS – may be displayed as a separate icon box which will link to chefs page with bios, Celeb Theatre timetable etc.
• TICKETS – either a button or clear callout to purchase tickets
• PLAN YOUR DAY – may be displayed in a separate content box which will then link through to getting there, sample itineraries and downloadable pocket show guide for visitors to print before coming to the Show.
• WHO’S EXHIBITING – to link back to city specific exhibitor lists

Our current website is out of date and has the following inadequacies (www.brightplatefair-example.com.au) -

The homepage
A city hub page
A general content page

1) Visitors

3) Media

Objectives:

Approach:

To be perceived as a fun, entertaining event with something for everyone - website creative and navigation must reflect this.

Other website examples:

Features

- New exhibitors section

‘CITY HUB’ BRIEF

- Dated design/layout
- Homepage too text heavy
- No content boxes that can be used for different features/areas (eg. News, Exhibitors etc)
- Uninspiring colours and skin(eg. grey background), does not reflect ‘a fun day out’
- Limited presence of social media platforms and lacks ‘community’
- No continuity in sub pages
- main banner too big – takes up too much space on homepage

Requirements
Must have
• As per above brief.

In addition:
Floating social media buttons on side
Wrap around image
Drop down menu (specifically for the location nav item)

```html
<!DOCTYPE html>
<html lang="en">
<head>
<meta charset="utf-8">
<title>Bright Plate &amp; Vine Fair</title>
<link rel="stylesheet" href="https://fonts.googleapis.com/css2?family=Didact+Gothic&family=Arimo:wght@400;700&display=swap">
<style>
:root{
  --sky-top:#8fd0f3;
  --sky-low:#d6eef8;
  --grass-light:#9fd23a;
  --grass-dark:#3f8a12;
  --page:#ffffff;
  --page-edge:#c9cfd3;
  --tab-blue:#2fa9e8;
  --tab-light:#8ed1f4;
  --panel-line:#d9dde0;
  --red:#b0101a;
  --text:#555555;
  --footer:#232323;
  --footer-text:#c4c4c4;
  --footer-head:#38b4ef;
  --rule:#7a7a7a;
  --dark-band:#2b2b2b;
}
*{box-sizing:border-box;margin:0;padding:0}
html,body{width:1200px;height:879px;overflow:hidden}
body{position:relative;font-family:"Arimo",Arial,sans-serif;color:var(--text);background:var(--sky-top)}
.backdrop{position:absolute;inset:0;background:linear-gradient(180deg,var(--sky-top) 0%,var(--sky-low) 62%,var(--grass-light) 74%,#6fb524 85%,var(--grass-dark) 100%)}
.page{position:absolute;left:105px;top:-20px;width:990px;height:742px;background:var(--page);border:6px solid var(--page-edge);border-top:none;border-radius:0 0 14px 14px;box-shadow:0 2px 6px rgba(0,0,0,.25)}
.abs{position:absolute}
.tabs{position:absolute;height:27px;border-bottom:3px solid var(--tab-blue)}
.tab{position:absolute;top:0;height:25px;border-radius:6px 6px 0 0;color:#fff;font-family:"Didact Gothic","Century Gothic",sans-serif;font-size:15px;line-height:27px;text-align:center;letter-spacing:.3px}
.tab.active{background:var(--tab-blue)}
.tab.active::after{content:"";position:absolute;left:50%;bottom:-9px;margin-left:-5px;border:5px solid transparent;border-top-color:var(--tab-blue)}
.tab.muted{background:var(--tab-light)}
.panel{position:absolute;border:1px solid var(--panel-line);border-top:none;border-radius:0 0 8px 8px}
.thumb{position:absolute;width:91px;height:78px;border:1px solid #bbb;padding:2px;background:#fff}
.thumb span{display:block;width:100%;height:100%}
.item-title{position:absolute;color:var(--red);font-family:"Didact Gothic","Century Gothic",sans-serif;font-size:13px}
.item-title.large{font-size:16px}
.item-text{position:absolute;width:188px;font-size:11.5px;line-height:18px;color:#444}
.item-text small{font-size:10px}
.read-more{position:absolute;color:var(--red);font-family:"Didact Gothic","Century Gothic",sans-serif;font-size:13px;text-decoration:underline}
.divider{position:absolute;height:0;border-top:1px dashed #c7c7c7}
.video{position:absolute;left:780px;top:-10px;width:300px;height:122px;background:var(--dark-band);border-radius:0 0 8px 8px;border:1px solid #bbb}
.video-frame{position:absolute;left:7px;top:0;width:284px;height:82px;background:linear-gradient(180deg,#9ac89a,#d9e5d0 60%,#b5c2b0)}
.controls{position:absolute;left:22px;top:50px;width:245px;height:24px}
.video-caption{position:absolute;left:10px;top:96px;color:#fff;font-family:"Didact Gothic","Century Gothic",sans-serif;font-size:12px}
.advert{position:absolute;left:780px;top:137px;width:300px;height:250px;border-radius:8px;overflow:hidden;border:1px solid #bbb;background:linear-gradient(90deg,#f1f1f1 0%,#e6e6e6 45%,#d4455a 70%,#4f9a3c 100%)}
.advert-name{position:absolute;left:9px;top:10px;width:140px;font-family:"Didact Gothic","Century Gothic",sans-serif;font-size:26px;line-height:29px;color:#333}
.advert-band{position:absolute;left:0;bottom:0;width:100%;height:74px;background:rgba(30,30,30,.85);color:#fff;padding:6px 12px}
.advert-band h3{font-family:"Didact Gothic","Century Gothic",sans-serif;font-weight:400;font-size:19px}
.advert-band p{font-size:11.5px;line-height:14px;margin-top:4px}
.footer{position:absolute;left:120px;top:424px;width:960px;height:275px;background:var(--footer)}
.col{position:absolute;top:16px}
.col h4{font-family:"Didact Gothic","Century Gothic",sans-serif;font-weight:400;font-size:15px;color:var(--footer-head);height:24px}
.rule{position:relative;height:2px;background:var(--rule);margin-left:2px}
.rule::after{content:"";position:absolute;left:10px;top:2px;border:5px solid transparent;border-top-color:var(--rule)}
.links{list-style:none;margin-top:20px;padding-left:8px}
.links li{font-size:11.5px;letter-spacing:.4px;line-height:20px;color:var(--footer-text);padding-left:9px;position:relative}
.links li::before{content:"";position:absolute;left:0;top:9px;width:3px;height:3px;background:#888}
.signup-copy{font-size:11.5px;line-height:20px;letter-spacing:.3px;color:var(--footer-text);margin:20px 0 0 3px;width:330px}
.email{position:absolute;left:3px;top:107px;width:243px;height:30px;border:1px solid #666;border-radius:6px;background:#3a3a3a;color:#8a8a8a;font-size:11.5px;line-height:28px;padding-left:9px}
.signup-btn{position:absolute;left:252px;top:107px;width:73px;height:30px;border-radius:6px;background:linear-gradient(#d11020,#8a0710);color:#fff;font-size:12px;line-height:30px;text-align:center}
.organiser{position:absolute;left:7px;top:166px;font-family:"Arimo",Arial,sans-serif;font-weight:700;font-size:19px;color:#fff;letter-spacing:.2px}
.fine{position:absolute;left:9px;font-size:11.5px;letter-spacing:.3px;color:var(--footer-text)}
</style>
</head>
<body>
<div class="backdrop" role="img" aria-label="Landscape skin: blue sky over rolling green grass hills"></div>
<div class="page"></div>

<!-- News -->
<div class="tabs" style="left:120px;top:18px;width:310px">
  <div class="tab active" style="left:0;width:69px">NEWS</div>
  <div class="tab muted" style="left:71px;width:116px">HIGHTLIGHT</div>
</div>
<div class="panel" style="left:120px;top:45px;width:310px;height:343px"></div>

<div class="thumb" style="left:131px;top:67px"><span role="img" aria-label="Photo of chefs plating food" style="background:linear-gradient(135deg,#d8d4cc,#7b7468)"></span></div>
<div class="item-title" style="left:235px;top:67px">Harlow &amp; Finch Celebrity</div>
<div class="item-text" style="left:237px;top:87px"><small>21 Feb 2012</small> Despite a drizzly start to the UK's...</div>
<div class="read-more" style="left:348px;top:132px">Read more</div>
<div class="divider" style="left:133px;top:160px;width:278px"></div>

<div class="thumb" style="left:131px;top:176px"><span role="img" aria-label="Photo of a wine theatre stage" style="background:linear-gradient(135deg,#3b3b3b,#8c8377)"></span></div>
<div class="item-title" style="left:235px;top:176px">Corvel Wine Theatre</div>
<div class="item-text" style="left:237px;top:196px"><small>2 June 2012</small> Despite a drizzly start to the UK's...</div>
<div class="read-more" style="left:348px;top:241px">Read more</div>
<div class="divider" style="left:133px;top:270px;width:278px"></div>

<div class="thumb" style="left:131px;top:286px"><span role="img" aria-label="Photo of visitors tasting wine" style="background:linear-gradient(135deg,#c9473e,#e8d6c8)"></span></div>
<div class="item-title" style="left:235px;top:286px">Ashbury Ridge Estates</div>
<div class="item-text" style="left:237px;top:306px"><small>15 Aug 2012</small> Despite a drizzly start to the UK's...</div>
<div class="read-more" style="left:348px;top:351px">Read more</div>

<!-- Exhibitors -->
<div class="tabs" style="left:450px;top:18px;width:310px">
  <div class="tab active" style="left:0;width:102px">EXIBITORS</div>
</div>
<div class="panel" style="left:450px;top:45px;width:310px;height:343px"></div>

<div class="thumb" style="left:461px;top:67px"><span role="img" aria-label="Photo of an exhibitor stand" style="background:linear-gradient(135deg,#3e7fc2,#d33a2e 70%,#eee)"></span></div>
<div class="item-title large" style="left:565px;top:65px">Harlow &amp; Finch Celebrity</div>
<div class="read-more" style="left:678px;top:132px">Read more</div>
<div class="divider" style="left:463px;top:160px;width:278px"></div>

<div class="thumb" style="left:461px;top:176px"><span role="img" aria-label="Photo of visitors at an exhibitor table" style="background:linear-gradient(135deg,#5a4a3e,#d9c7b2)"></span></div>
<div class="item-title large" style="left:565px;top:174px">Harlow &amp; Finch Celebrity</div>
<div class="read-more" style="left:678px;top:241px">Read more</div>
<div class="divider" style="left:463px;top:270px;width:278px"></div>

<div class="thumb" style="left:461px;top:286px"><span role="img" aria-label="Photo of a cooking class" style="background:linear-gradient(135deg,#4a4a4a,#c8b9a6)"></span></div>
<div class="item-title large" style="left:565px;top:284px">Harlow &amp; Finch Celebrity</div>
<div class="read-more" style="left:678px;top:351px">Read more</div>

<!-- Video -->
<div class="video">
  <div class="video-frame" role="img" aria-label="Video still from the show floor"></div>
  <svg class="controls" viewBox="0 0 245 24" aria-hidden="true">
    <rect x="0" y="0" width="27" height="24" rx="2" fill="#111"/>
    <polygon points="9,5 20,12 9,19" fill="#fff"/>
    <rect x="36" y="0" width="172" height="24" rx="2" fill="#111"/>
    <rect x="45" y="11" width="61" height="3" fill="#fff"/>
    <text x="115" y="16" fill="#fff" font-size="10" font-family="Arial,sans-serif">00:00</text>
    <g fill="#35a9e6"><rect x="152" y="7" width="3" height="10"/><rect x="157" y="7" width="3" height="10"/><rect x="162" y="7" width="3" height="10"/><rect x="167" y="7" width="3" height="10"/><rect x="172" y="7" width="3" height="10"/><rect x="177" y="7" width="3" height="10"/><rect x="182" y="7" width="3" height="10"/><rect x="187" y="7" width="3" height="10"/><rect x="192" y="7" width="3" height="10"/></g>
    <rect x="217" y="0" width="27" height="24" rx="2" fill="#111"/>
    <path d="M224 7h4M224 7v4M237 7h-4M237 7v4M224 18h4M224 18v-4M237 18h-4M237 18v-4" stroke="#fff" stroke-width="2"/>
  </svg>
  <div class="video-caption">Bright Plate &amp; Vine Fair</div>
</div>

<!-- Advert -->
<div class="advert" role="img" aria-label="Advert: fresh berries, tomatoes and mint leaves with a red ribbon">
  <div class="advert-name">Bright Plate &amp; Vine Fair</div>
  <div class="advert-band">
    <h3>EXIBITORS NAME</h3>
    <p>It is a long established fact that a reader will be distracted by the readable content of a page</p>
  </div>
</div>

<!-- Footer -->
<footer class="footer">
  <div class="col" style="left:19px;width:181px">
    <h4>Bright Plate &amp; Vine Fair</h4><div class="rule"></div>
    <ul class="links"><li>Home</li><li>Melbourne</li><li>Sydney</li><li>Perth</li><li>Adelaide</li><li>Brisbane</li><li>Want to Exhibit?</li><li>Recipe Club</li></ul>
  </div>
  <div class="col" style="left:230px;width:154px">
    <h4>Show Attractions</h4><div class="rule"></div>
    <ul class="links"><li>Celebrity Theatre</li><li>Cheese Masterclass</li><li>Cooking School</li><li>Decanter Bar</li><li>Restaurant</li><li>Wine Theatre</li><li>Exhibitor list</li><li>Floor plans</li></ul>
  </div>
  <div class="col" style="left:410px;width:151px">
    <h4>Chef Bio's</h4><div class="rule"></div>
    <ul class="links"><li>Lena Marsh</li><li>Colin Havers</li><li>Peter Anastas</li><li>Remy Fournel</li><li>Sam Doran</li><li>Toby Pennick</li></ul>
    <h4 style="margin-top:16px">Recipe Club</h4><div class="rule"></div>
    <ul class="links"><li>Login</li></ul>
  </div>
  <div class="col" style="left:590px;width:350px;height:250px">
    <h4>Newsletter Signup</h4><div class="rule"></div>
    <p class="signup-copy">Register to receive our newsletter, bringing you exclusive offers and the latest news.</p>
    <div class="email">Enter Your Email</div>
    <div class="signup-btn">Sign Up</div>
    <div class="organiser">meridian</div>
    <p class="fine" style="top:200px">Event organised by Meridian Events Australia.© 2007.</p>
    <p class="fine" style="top:235px">Competition Terms &amp; Conditions</p>
  </div>
</footer>
</body>
</html>
```